Property Developer - Simple yet Sophisticated and Sharp Business Card

We are a medium sized property developer involved mainly in townhouse developments and land subdivisions.

The company is looking for a simple, sharp and sophisticated business card that will be given to contractors, land owners, financiers etc and thus will need to look professional.

Property development related graphics and art can be used, however the card is not to be too "busy" or crowded. Our company name is KL Estates which could possibly be incorporated into the graphics or artwork.

Single sided and/or double sided designs will be acceptable.

A Simple, Sophisticated, Sharp design please!

Good Luck !

```html
<!DOCTYPE html>
<html lang="en">
<head>
<meta charset="UTF-8">
<title>KL Estates – Business Card</title>
<link rel="stylesheet" href="https://fonts.googleapis.com/css2?family=Arimo:wght@400;700&display=swap">
<style>
  :root {
    --stage: #2b2b2d;
    --blue-light: #2a8ee0;
    --blue-mid: #157ad0;
    --blue-deep: #0a5aa8;
    --name-blue: #1b7cc8;
    --paper: #ffffff;
    --ink: #111111;
  }
  * { margin: 0; padding: 0; box-sizing: border-box; }
  html, body {
    width: 1200px;
    height: 1052px;
    overflow: hidden;
    background: var(--stage);
  }
  .canvas {
    position: relative;
    width: 1200px;
    height: 1052px;
  }
  .card {
    position: absolute;
    left: 200px;
    width: 800px;
    height: 457px;
    box-shadow: 0 10px 28px rgba(0, 0, 0, 0.45);
    overflow: hidden;
  }
  .card--front {
    top: 44px;
    background: radial-gradient(ellipse at 45% 45%, var(--blue-light) 0%, var(--blue-mid) 45%, var(--blue-deep) 100%);
  }
  .card--back {
    top: 551px;
    background: var(--paper);
  }
  .company-name {
    position: absolute;
    font-family: "Arimo", Arial, sans-serif;
    font-weight: 700;
    line-height: 1;
    white-space: nowrap;
  }
  .card--front .company-name {
    left: 170px;
    top: 190px;
    font-size: 72px;
    color: var(--paper);
  }
  .card--back .company-name {
    left: 34px;
    top: 345px;
    font-size: 48px;
    color: var(--ink);
  }
  .holder {
    position: absolute;
    right: 40px;
    top: 52px;
    text-align: right;
    font-family: "Arimo", Arial, sans-serif;
  }
  .holder__name {
    font-size: 26px;
    color: var(--name-blue);
    line-height: 1.2;
  }
  .holder__title {
    font-size: 16px;
    color: var(--ink);
    margin-top: 4px;
  }
  .contact {
    position: absolute;
    right: 40px;
    bottom: 40px;
    text-align: right;
    font-family: "Arimo", Arial, sans-serif;
    font-size: 15px;
    line-height: 1.45;
    color: var(--ink);
    list-style: none;
  }
  .contact__label { font-weight: 700; }
</style>
</head>
<body>
<main class="canvas">
  <section class="card card--front" aria-label="Card front">
    <p class="company-name">KL Estates</p>
  </section>

  <section class="card card--back" aria-label="Card back">
    <div class="holder">
      <p class="holder__name">Daniel Marsh</p>
      <p class="holder__title">director</p>
    </div>
    <p class="company-name">KL Estates</p>
    <ul class="contact">
      <li><span class="contact__label">Phone:</span> (07) 5550 1824</li>
      <li><span class="contact__label">Fax:</span> (07) 5550 1937</li>
      <li><span class="contact__label">Email:</span> projects.klestates@mailbox.com</li>
      <li><span class="contact__label">Postal:</span> PO Box 2718 Riverton East QLD 4120</li>
    </ul>
  </section>
</main>
</body>
</html>
```